Brisk Mend's Blow Their Mind Website

We own a group of cell phone and tablet repair shops in the bay area that is emerging into the mobile device insurance industry and want to develop a site that is clean, organized, and efficient at communicating who we are, the services we provide and the positive feedback we have been getting from our clients. As we enter into this new field of business, Our goal is to attract larger corporate accounts.

We want our home screen to have a big focus on the protection plan for the devices right away much like the home screen from these links:

http://www.gadgetvault.com/

and also - https://us.keepitsnug.com/smartphone-protection.html

We also need to make our repair services clear, here is a website of a company that does repair and we want to highlight both ends of the business.

ww.fixnovo.com

So the home screen will include the tab categories at the top of the screen
home/ protection /repair /about /contact

The first portion will be protection and as you scroll down there will be the next section about repair and following that will be information about the company.

Target Market(s)

Individuals that would be looking for pricing, clients that come to our store, but ultimately the heavy hitters we would want to attract would be larger corporate accounts so the message we want to communicate is professional, organized and credible in the services we provide.

Industry/Entity Type

Cell Phone

Number of Pages Required

5+ page

Font styles to use
Serif

Colors
34a6d7

Requirements
Must have
• Eye catching, organized, with the wow factor that a business will look at our site and will be able to tell that we know what looks good and what grabs peoples attention. A large emphasis on the protection plan section like the links we provided and an organized home screen with the sections highlighted in the project description
• Tabs with links to different sections of the business such as protection that will go into detail about our protections plans and why our plan is best
• repair with a menu of the different prices we provide for different devices and services for that device
• an about us tab
• a contact us tab
Nice to have
• Artistic flow on the homescreen that the different sections flow together without looking too cookie cutter
• Wow factor
Should not have
• Clutter, confusion, disorganization, cheesy cookie cutter

```html
<!DOCTYPE html>
<html lang="en">
<head>
<meta charset="utf-8">
<title>Brisk Mend – Protection Plans and Repair</title>
<link href="https://fonts.googleapis.com/css2?family=Open+Sans:wght@400;600;700;800&display=swap" rel="stylesheet">
<style>
:root{
  --blue:#1e9de0;
  --blue-light:#49b8ee;
  --blue-deep:#0d7fc6;
  --ink:#222628;
  --text:#555b60;
  --muted:#8a9095;
  --line:#dfe3e6;
  --row-alt:#f4f6f7;
  --white:#ffffff;
}
*{box-sizing:border-box;margin:0;padding:0}
html,body{width:885px;height:1200px;overflow:hidden}
body{font-family:"Open Sans",Arial,sans-serif;color:var(--text);background:var(--white);position:relative}

/* header */
.site-header{position:absolute;top:0;left:0;width:885px;height:72px;display:flex;align-items:center;justify-content:space-between;padding:0 225px 0 228px}
.brand{display:flex;align-items:center;gap:8px;font-weight:700;font-size:19px;color:var(--blue)}
.brand-dot{width:22px;height:22px;border-radius:50%;background:var(--blue)}
.main-nav{display:flex;gap:12px;font-size:9px;font-weight:600;text-transform:uppercase;color:var(--muted)}
.main-nav .current{color:var(--blue);border-bottom:1px solid var(--blue)}

/* hero */
.hero{position:absolute;top:72px;left:0;width:885px;height:275px;background:radial-gradient(ellipse at 55% 40%,var(--blue-light),var(--blue) 55%,var(--blue-deep))}
.hero-device{position:absolute;left:232px;top:20px;width:170px;height:240px;border-radius:18px;background:linear-gradient(135deg,#e9eef2,#9aa7b1 60%,#3a4650)}
.hero-copy{position:absolute;left:432px;top:28px;width:210px;color:var(--white)}
.hero-title{font-size:22px;line-height:24px;font-weight:800;text-transform:uppercase}
.hero-lead{font-size:7.5px;line-height:11px;margin:10px 0 8px;opacity:.9}
.hero-points{list-style:none;font-size:7.5px;line-height:13px}
.hero-points li::before{content:"";display:inline-block;width:5px;height:5px;border-radius:50%;background:var(--white);margin-right:6px}
.btn-dark{display:inline-block;margin-top:12px;background:var(--ink);color:var(--white);font-size:8px;font-weight:700;text-transform:uppercase;padding:6px 12px}
.price-box{position:absolute;left:662px;top:80px;width:166px;height:90px;background:rgba(10,60,100,.45);text-align:center;color:var(--white);padding-top:14px}
.price-box .price{font-size:15px;font-weight:700}
.price-box .btn-dark{margin-top:12px;padding:8px 16px}

/* who we are */
.about{position:absolute;top:365px;left:221px;width:443px;text-align:center}
.section-title{font-size:11px;font-weight:800;color:var(--ink);text-transform:uppercase;letter-spacing:.5px}
.about-text{font-size:7.5px;line-height:11px;margin-top:12px;color:var(--muted)}
.services{display:grid;grid-template-columns:1fr 1fr;row-gap:28px;margin-top:26px}
.service svg{width:44px;height:44px}
.service-label{font-size:8.5px;font-weight:600;text-transform:uppercase;color:var(--text);margin-top:8px}

/* pricing table */
.plans{position:absolute;top:692px;left:221px;width:443px;border-collapse:collapse;font-size:7px}
.plans th{background:var(--ink);color:var(--white);font-weight:600;height:34px;font-size:8px;line-height:11px}
.plans th small{display:block;font-size:6px;font-weight:400;opacity:.75}
.plans th:first-child{text-align:left;padding-left:12px;width:46%}
.plans th+th{border-left:1px solid #444}
.plans td{height:48px;border-bottom:1px solid var(--line);vertical-align:middle;text-align:center}
.plans td:first-child{text-align:left;padding:0 12px;color:var(--muted);line-height:9px}
.plans td:first-child b{display:block;color:var(--ink);font-size:7.5px}
.plans tr:nth-child(even) td{background:var(--row-alt)}
.tick{width:12px;height:12px}

/* reviews */
.reviews{position:absolute;top:1005px;left:221px;width:443px;text-align:center}
.avatar{width:56px;height:56px;border-radius:50%;margin:12px auto 8px;background:linear-gradient(#c9d3db,#7f8d98);border:3px solid var(--white);box-shadow:0 0 0 1px var(--line)}
.reviewer{font-size:7px;color:var(--blue);text-transform:uppercase}
.quote{font-size:7.5px;line-height:11px;color:var(--muted);margin-top:8px}
.dots{display:flex;justify-content:center;gap:5px;margin-top:10px}
.dots span{width:5px;height:5px;border-radius:50%;background:var(--line)}
.dots span.on{background:var(--blue)}

/* footer */
.site-footer{position:absolute;top:1162px;left:0;width:885px;height:38px;background:var(--blue);display:flex;align-items:center;justify-content:space-between;padding:0 225px 0 228px}
.footer-nav{display:flex;gap:10px;font-size:7.5px;color:var(--white)}
.social{display:flex;gap:6px}
.social span{width:16px;height:16px;border-radius:50%;background:var(--white)}
</style>
</head>
<body>

<header class="site-header">
  <div class="brand"><span class="brand-dot"></span>Brisk Mend</div>
  <nav class="main-nav">
    <span class="current">Home</span><span>About</span><span>Repair</span><span>Product</span><span>Contact</span>
  </nav>
</header>

<section class="hero">
  <div class="hero-device" role="img" aria-label="Photo of a smartphone with a cracked screen"></div>
  <div class="hero-copy">
    <h1 class="hero-title">Protection plan for your smartphone</h1>
    <p class="hero-lead">Keep your phone covered against drops, spills and theft with one simple monthly plan that fits every budget and device.</p>
    <ul class="hero-points">
      <li>Covering drops up to 6 years old</li>
      <li>Same-day repair replacement</li>
      <li>Unlimited claims</li>
      <li>Low-cost coverage for all devices</li>
    </ul>
    <span class="btn-dark">Product</span>
  </div>
  <div class="price-box">
    <div class="price">From $5.00 a month</div>
    <span class="btn-dark">Get a quote</span>
  </div>
</section>

<section class="about">
  <h2 class="section-title">Who we are</h2>
  <p class="about-text">We are a group of phone and tablet repair shops across the bay area, now bringing the same care to device protection. Our technicians have fixed thousands of screens, batteries and boards, and our plans are built around fast, honest service. Whether you walk into our store or manage hundreds of company devices, we keep your team connected with clear pricing, quick turnaround and support you can count on every day.</p>
  <div class="services">
    <div class="service">
      <svg viewBox="0 0 44 44" fill="none" stroke="var(--blue)" stroke-width="2.5"><rect x="13" y="4" width="18" height="36" rx="3"/><line x1="19" y1="35" x2="25" y2="35"/></svg>
      <div class="service-label">Damage insurance</div>
    </div>
    <div class="service">
      <svg viewBox="0 0 44 44" fill="none" stroke="var(--blue)" stroke-width="2.5"><path d="M22 4 C22 4 10 20 10 28 a12 12 0 0 0 24 0 C34 20 22 4 22 4Z"/></svg>
      <div class="service-label">Liquid &amp; water damage</div>
    </div>
    <div class="service">
      <svg viewBox="0 0 44 44" fill="none" stroke="var(--blue)" stroke-width="2.5"><circle cx="17" cy="17" r="9"/><circle cx="17" cy="17" r="3"/><circle cx="31" cy="31" r="7"/><circle cx="31" cy="31" r="2"/></svg>
      <div class="service-label">Damage insurance</div>
    </div>
    <div class="service">
      <svg viewBox="0 0 44 44" fill="none" stroke="var(--blue)" stroke-width="2.5"><rect x="6" y="9" width="32" height="29" rx="2"/><line x1="6" y1="17" x2="38" y2="17"/><line x1="14" y1="5" x2="14" y2="12"/><line x1="30" y1="5" x2="30" y2="12"/><path d="M13 24h4M20 24h4M27 24h4M13 30h4M20 30h4"/></svg>
      <div class="service-label">Liquid &amp; water damage</div>
    </div>
  </div>
</section>

<table class="plans">
  <thead>
    <tr>
      <th>Protection plan Pricing and Benefits</th>
      <th>Protection plan 1<small>$5.00 a month for all devices</small></th>
      <th>Protection plan 2<small>$8.00 a month for all devices</small></th>
    </tr>
  </thead>
  <tbody>
    <tr><td><b>Loss &amp; Theft</b>Get a new phone fast if yours is lost or stolen</td>
      <td><svg class="tick" viewBox="0 0 12 12"><path d="M2 6l3 3 5-6" fill="none" stroke="var(--blue)" stroke-width="2"/></svg></td>
      <td><svg class="tick" viewBox="0 0 12 12"><path d="M2 6l3 3 5-6" fill="none" stroke="var(--blue)" stroke-width="2"/></svg></td></tr>
    <tr><td><b>One-time Battery Replacement</b>A fresh battery once your old one starts to fade, no extra charge</td>
      <td><svg class="tick" viewBox="0 0 12 12"><path d="M2 6l3 3 5-6" fill="none" stroke="var(--blue)" stroke-width="2"/></svg></td>
      <td><svg class="tick" viewBox="0 0 12 12"><path d="M2 6l3 3 5-6" fill="none" stroke="var(--blue)" stroke-width="2"/></svg></td></tr>
    <tr><td><b>Speed Drive and Fast</b>Priority service with same-day repair and free return shipping</td>
      <td></td>
      <td><svg class="tick" viewBox="0 0 12 12"><path d="M2 6l3 3 5-6" fill="none" stroke="var(--blue)" stroke-width="2"/></svg></td></tr>
    <tr><td><b>Mechanical Failure</b>Covers buttons, ports and parts that stop working over time</td>
      <td><svg class="tick" viewBox="0 0 12 12"><path d="M2 6l3 3 5-6" fill="none" stroke="var(--blue)" stroke-width="2"/></svg></td>
      <td><svg class="tick" viewBox="0 0 12 12"><path d="M2 6l3 3 5-6" fill="none" stroke="var(--blue)" stroke-width="2"/></svg></td></tr>
    <tr><td><b>Accidental Damage</b>Cracked screens and spills fixed by our own technicians</td>
      <td></td>
      <td><svg class="tick" viewBox="0 0 12 12"><path d="M2 6l3 3 5-6" fill="none" stroke="var(--blue)" stroke-width="2"/></svg></td></tr>
  </tbody>
</table>

<section class="reviews">
  <h2 class="section-title">Customer reviews</h2>
  <div class="avatar" role="img" aria-label="Portrait of a customer"></div>
  <div class="reviewer">Satisfied customer</div>
  <p class="quote">Quick, friendly and fair. My cracked screen was fixed within the hour, and the protection plan has already saved me twice. I now send my whole office team here for every phone and tablet.</p>
  <div class="dots"><span></span><span class="on"></span><span></span></div>
</section>

<footer class="site-footer">
  <nav class="footer-nav"><span>Home</span><span>About</span><span>Repair</span><span>Product</span><span>Contact</span></nav>
  <div class="social"><span></span><span></span><span></span><span></span></div>
</footer>

</body>
</html>
```